Music Festival in Colorado Needs Awesome Flier Design

We need an eye-catching & captivating flier design for an annual music festival in Denver, CO (USA). The festival features the best Colorado musicians within the genres of jam - funk - bluegrass - electronic - reggae - rock.

The design should look clean and professional while still being creative and unique. The past three years' flier designs are attached, as well as the logo and some other designs that match the aesthetic of what we're looking for.

This festival has a big element of Colorado pride so any

Target Market(s)

Hippies - live music enthusiasts - partiers. Ages 21 - 40.

Industry/Entity Type

Entertainment

Colors
0355a3
ec1f27
ffffff
fbed22

Requirements
Must have
• Attached design text.
Nice to have
• - Quality texture and psychedelic elements.
• - Colorado pride elements; color scheme (red, white, blue & yellow), flag, ect.
• - Nature elements are awesome but this is also a downtown festival so keep that in mind.
Should not have
• Cheesy artwork.

```html
<!DOCTYPE html>
<html lang="en">
<head>
<meta charset="utf-8">
<title>Echo Hollow – Front Range Sound Gathering</title>
<link href="https://fonts.googleapis.com/css2?family=Oswald:wght@400;600;700&display=swap" rel="stylesheet">
<style>
  :root {
    --paper: #ffffff;
    --sky-top: #4e2f63;
    --sky-mid: #b0607a;
    --sky-warm: #f0b07a;
    --sky-pale: #f7efc8;
    --ink: #3a1d48;
    --sunset: #e98a3c;
    --dusk: #6a3560;
    --night: #3b1f4a;
    --gold: #f6d65a;
    --white: #ffffff;
  }
  * { box-sizing: border-box; margin: 0; padding: 0; }
  html, body { width: 796px; height: 1200px; overflow: hidden; background: var(--paper); }
  body { font-family: "Oswald", "Arial Narrow", sans-serif; }

  .poster {
    position: absolute; left: 27px; top: 21px; width: 742px; height: 1152px;
    overflow: hidden;
    background: linear-gradient(180deg, var(--sky-top) 0%, var(--sky-mid) 14%, var(--sky-warm) 22%, var(--sky-pale) 32%, var(--sky-pale) 58%, var(--sky-warm) 66%);
  }

  .megaphone {
    position: absolute; top: 62px; width: 130px; height: 72px;
    background: var(--white); border-radius: 6px;
  }
  .megaphone.left { left: 44px; }
  .megaphone.right { right: 44px; }

  .dates {
    position: absolute; top: 26px; width: 100%; text-align: center;
    color: var(--white); font-weight: 600; letter-spacing: 2px; line-height: 1.15;
    font-size: 20px;
  }

  .festival-name {
    position: absolute; top: 84px; width: 100%; text-align: center; color: var(--white);
    font-weight: 700; text-transform: uppercase;
  }
  .festival-name .small { display: block; font-size: 34px; letter-spacing: 4px; line-height: 1; }
  .festival-name .big { display: block; font-size: 104px; line-height: 0.98; letter-spacing: 3px; }
  .festival-name .tag {
    display: inline-block; font-size: 14px; letter-spacing: 4px; margin-top: 6px;
    padding: 3px 14px; border: 2px solid var(--white);
  }

  .lineup {
    position: absolute; top: 296px; left: 24px; right: 24px; text-align: center;
    color: var(--ink); font-weight: 700; text-transform: uppercase;
  }
  .lineup p { white-space: nowrap; }
  .headliners { font-size: 33px; line-height: 1.2; }
  .support { font-size: 20px; line-height: 1.3; margin-top: 4px; }
  .lineup .last { font-size: 25px; margin-top: 2px; }

  .landscape {
    position: absolute; left: 0; right: 0; top: 640px; height: 450px;
    background: linear-gradient(180deg, rgba(233,138,60,0) 0%, var(--sunset) 22%, #d9703f 45%, var(--dusk) 70%, var(--night) 100%);
  }

  .venue-bar {
    position: absolute; left: 0; right: 0; bottom: 0; height: 70px;
    background: var(--night); color: var(--gold); text-align: center;
    font-weight: 600; letter-spacing: 1px; padding-top: 12px;
  }
  .venue-bar .address { font-size: 19px; line-height: 1.2; }
  .venue-bar .web { font-size: 13px; }
</style>
</head>
<body>
  <main class="poster">
    <div class="megaphone left" role="img" aria-label="Megaphone illustration pointing inward"></div>
    <div class="megaphone right" role="img" aria-label="Megaphone illustration pointing inward"></div>

    <header class="dates">
      <div>6TH ANNUAL</div>
      <div>MAY 11TH – 13TH 2018</div>
    </header>

    <h1 class="festival-name">
      <span class="small">Echo</span>
      <span class="big">Hollow</span>
      <span class="tag">Front Range Sound Gathering</span>
    </h1>

    <section class="lineup">
      <div class="headliners">
        <p>Jory Vance Band • Every Hand</p>
        <p>Orchestra • Brake Ledger • The</p>
        <p>Copper Beans • T-Rook &amp; The Crest</p>
      </div>
      <div class="support">
        <p>Tinfoil Orchestra • Sagebrick • Dynoquartz</p>
        <p>Whitecap Ramble • Emberline Ensemble • Velvet</p>
        <p>Kite • The Barley Yard • Skywick • Marrowby • Hollowkin</p>
        <p>Pollenroot • Ridge Depot • Spindles • The Thistle Sisters</p>
        <p>Juniper Drum • Talia Corbin Band • Atomhaus • Turtlewick</p>
        <p>Dubasaurus • Other Amber • The Idlers Co. • Mama Clementine</p>
        <p>Ninth Ridge Division • Amorluz • Indigo Alo • Groove</p>
        <p>Wooly Moth • Idle Commodore • Rusty Thunderhead • Willowsett</p>
        <p>Signal 517 • Crestline Vibe • Prismshift • Cory Rusk &amp; The Soul Barn</p>
        <p class="last">Lumen Rising • Mbira Sky</p>
      </div>
    </section>

    <div class="landscape" role="img" aria-label="Sunset mountain range with birds and a city skyline in silhouette"></div>

    <footer class="venue-bar">
      <div class="address">Marten Street Yard – Denver, Co 80299 – 611 W. 46th Ave</div>
      <div class="web">Tickets &amp; More Info @ www.echohollowfest.com</div>
    </footer>
  </main>
</body>
</html>
```